Brookside Grocer

Hope all is well!

Wanted to make business cards for my father. His name is Faisal Qureshi and owns convenience stores. I have attached logo :)

He does not want any title just simple name and phone. An email would be nice as well.

Faisal Qureshi
Cell: 413-585-2046
Store: 413-719-4820

Brooksidegrocer512@fernpost.com

The design and style is totally up to you :) The colors we were looking for were the same as logo :)

```html
<!DOCTYPE html>
<html lang="en">
<head>
<meta charset="utf-8">
<title>Brookside Grocer – Business Card</title>
<link href="https://fonts.googleapis.com/css2?family=Montserrat:wght@400;500;700&display=swap" rel="stylesheet">
<style>
  :root {
    --navy: #203673;
    --red: #e2333c;
    --paper: #f4f4f4;
    --white: #ffffff;
    --backdrop: #1b1b1b;
  }
  * { margin: 0; padding: 0; box-sizing: border-box; }
  html, body {
    width: 1200px; height: 1059px; overflow: hidden;
    background: var(--backdrop);
    font-family: "Montserrat", Arial, sans-serif;
  }
  .stage { position: relative; width: 1200px; height: 1059px; }
  .card {
    position: absolute; left: 255px; width: 690px; height: 392px;
    border-radius: 18px; overflow: hidden;
  }
  .card--front { top: 89px; background: var(--paper); }
  .card--back { top: 548px; background: var(--navy); }
  .card__wave { position: absolute; inset: 0; width: 100%; height: 100%; }
  .brand-name {
    position: absolute; font-weight: 700; line-height: 1.05;
    letter-spacing: 0.5px; text-align: center;
  }
  .card--front .brand-name {
    right: 42px; top: 58px; width: 280px;
    color: var(--navy); font-size: 34px;
  }
  .card--back .brand-name {
    left: 0; right: 0; top: 140px;
    color: var(--white); font-size: 56px;
  }
  .contact { position: absolute; left: 36px; top: 220px; color: var(--white); }
  .contact__name { color: var(--red); font-weight: 700; font-size: 25px; }
  .contact__rule { width: 12px; height: 1.5px; background: var(--red); margin: 14px 0 14px; }
  .contact__line {
    display: flex; align-items: center; gap: 7px;
    font-size: 16.5px; font-weight: 400; height: 28.5px;
  }
  .contact__line svg { width: 12px; height: 12px; fill: var(--red); flex: none; }
  .contact__tag { color: var(--red); font-size: 11.5px; margin-left: 3px; }
</style>
</head>
<body>
<main class="stage">
  <section class="card card--front">
    <svg class="card__wave" viewBox="0 0 690 392" preserveAspectRatio="none" aria-hidden="true">
      <path d="M0 196 C60 158 110 145 170 150 C270 158 380 250 470 280 C540 300 620 290 690 240 L690 392 L0 392 Z" fill="var(--navy)"/>
      <path d="M0 182 C50 148 110 134 170 140 C200 143 230 150 250 158 C200 146 150 142 110 150 C70 158 30 170 0 186 Z" fill="var(--red)"/>
      <path d="M84 152 C180 140 280 190 360 230 C410 256 460 288 505 308 C450 290 400 262 350 240 C260 200 170 150 84 152 Z" fill="var(--navy)"/>
      <path d="M431 263 C520 290 620 280 690 218 L690 226 C620 280 520 290 431 263 Z" fill="var(--red)"/>
    </svg>
    <div class="brand-name">Brookside Grocer</div>
    <div class="contact">
      <div class="contact__name">Faisal Qureshi</div>
      <div class="contact__rule"></div>
      <div class="contact__line">
        <svg viewBox="0 0 24 24"><path d="M6.6 10.8a15.2 15.2 0 0 0 6.6 6.6l2.2-2.2c.3-.3.7-.4 1-.2 1.1.4 2.3.6 3.6.6.6 0 1 .4 1 1V20c0 .6-.4 1-1 1A17 17 0 0 1 3 4c0-.6.4-1 1-1h3.5c.6 0 1 .4 1 1 0 1.3.2 2.5.6 3.6.1.3 0 .7-.2 1z"/></svg>
        413-585-2046 <span class="contact__tag">(Call)</span>
      </div>
      <div class="contact__line">
        <svg viewBox="0 0 24 24"><path d="M2 9c2-3 6-4 10-4s8 1 10 4l-2 3-4-1V8H8v3l-4 1zM6 13h12l2 7H4z"/></svg>
        413-719-4820 <span class="contact__tag">(Store)</span>
      </div>
      <div class="contact__line">
        <svg viewBox="0 0 24 24"><path d="M2 10l10-7 10 7v11H2zm2 2v7h16v-7l-8 5z"/></svg>
        Brooksidegrocer512@fernpost.com
      </div>
    </div>
  </section>
  <section class="card card--back">
    <div class="brand-name">Brookside Grocer</div>
  </section>
</main>
</body>
</html>
```